VitalHaven.Studio - Trifold Brochure

Requirements: Phase 1 - Trifold brochure (in the spirit of existing brand look and feel). [Phase - subject to the success of Phase 1 - leaflet design with services, business card design - not to be quoted in this task] . Phase 3 - One page website

Yet to be launched concept VitalHaven.Studio (will launch in 2 days), has been established initially to serve a very specific audience - women, 30s-40s, with seeking higher levels fo wellness. Already settled with the alternative health modalities, but desperate for more energy, needing direction on their path, and potentially support and care in the form of coaching and mentoring.

The clinic is launching with a unique offer, using technology to assess for areas of their life, mind and body that need attention. The technology is being offered for Free, Lifetime, Unlimited Access to those who buy a small piece of hardware that is able to "read" how their body is working. It can be used by more than one person (useful for families)

The technology is not owned by the clinic, only licensed by. The clinic facilitates the onboarding of the client to the platform and teaches the how to read it, and navigate the instructions contained within to improve energy. .There are other services available from the clinic which are higher touch - 30 and 90 day protocols including, health strategy, accountability, which drive deeper transformation.

Some design work has been done .
I need a designer to carry on from the prior designer, on a tight deadline for this Phase.

We have logo, brand colours and double sided leaflet that will help understand the look and feel of the brand.

This Phase is about Trifold DL. Despite all services being delivered online, the launch and this project relates to the launch which will be run out of an offline clinic (joint venture partner) . This brochure will be handed to the client on completing their initial scan (for free) and given their access to their online account.

This brochure should show case the clinic, a few testimonials,
the practitioner behind the clinic, call to action is move along the path step by step...will outline.

I need a designer to take the existing brand concept, and help me build the trifold brochure with a 48 hour deadline, so that we may move to Phase 2 & 3 of the launch project. I want to just focus on the trifold at this stage.

Need extra days to review

Here is the link to the Brightgrid Sheet again https://files.examplecloud.net/sheets/d/7qTr-Kc2LMNpawXz84RdBuvE93hoxYtVQ1JmKP5Sg2nu/view?usp=sharing

Target Market(s)

Women aged 30-50

Industry/Entity Type

Health And Wellness

Colors
88d0c7
33a6d7
3176b5

Requirements
Must have
• Draw from colour palette provided - se two page brochure as a guideline
Broad lay out per the powerpoint provided
Should not have
• no pictures of men

```html
<!DOCTYPE html>
<html lang="en">
<head>
<meta charset="utf-8">
<title>VitalHaven.Studio – Trifold Brochure Outside</title>
<link href="https://fonts.googleapis.com/css2?family=Montserrat:ital,wght@0,400;0,500;0,600;0,700;1,400&family=Oswald:wght@400;600&display=swap" rel="stylesheet">
<style>
  :root{
    --teal:#88d0c7;
    --sky:#33a6d7;
    --blue:#3176b5;
    --navy:#245f98;
    --ink:#2a2a2a;
    --paper:#ffffff;
    --mist:#eef0f2;
    --stage:#3b3b3d;
  }
  *{box-sizing:border-box;margin:0;padding:0}
  html,body{width:829px;height:1200px;overflow:hidden;background:var(--stage)}
  body{font-family:"Montserrat",sans-serif;color:var(--ink);position:relative}
  .brochure{position:absolute;left:26px;top:324px;width:777px;height:552px;background:var(--paper);overflow:hidden;box-shadow:0 6px 24px rgba(0,0,0,.35)}
  .panel{position:absolute;top:0;width:259px;height:552px}
  .panel--about{left:0;background:var(--paper)}
  .panel--testimonials{left:259px;background:linear-gradient(180deg,#f4f5f6,#e8eaec)}
  .panel--cover{left:518px;background:var(--paper)}
  .swoosh{position:absolute;left:0;top:0;width:777px;height:140px}
  .abs{position:absolute}

  /* about panel */
  .portrait{position:absolute;left:0;top:0;width:259px;height:200px}
  .practitioner-name{position:absolute;top:204px;width:100%;text-align:center;font-weight:700;font-size:18.5px;color:var(--blue);letter-spacing:.3px}
  .practitioner-creds{position:absolute;top:228px;width:100%;text-align:center;font-size:9.5px;font-weight:500}
  .practitioner-rule{position:absolute;top:244px;left:106px;width:48px;height:1.5px;background:var(--navy)}
  .bio{position:absolute;left:24px;top:254px;width:216px;font-size:7.1px;line-height:9.4px;text-align:justify}
  .bio p{margin-bottom:3.4px}
  .bio strong{font-weight:600}
  .footer{position:absolute;bottom:0;left:0;width:100%;height:34px;color:#fff;font-size:9px;letter-spacing:1.6px;text-align:center;line-height:34px}
  .footer--sky{background:var(--sky)}
  .footer--blue{background:var(--blue)}
  .footer--navy{background:rgba(25,64,104,.92)}

  /* testimonials panel */
  .pill{position:absolute;background:var(--navy);color:#fff;font-weight:700;border-radius:14px;text-align:center}
  .pill--testimonials{left:57px;top:25px;width:143px;height:23px;line-height:23px;font-size:12px;letter-spacing:.3px}
  .quote-mark{position:absolute;left:32px;top:60px;font-family:"Oswald",sans-serif;font-size:30px;color:#c9cdd2;line-height:1}
  .testimonial{position:absolute;left:35px;width:188px;font-style:italic;font-size:7.4px;line-height:9.6px}
  .testimonial cite{display:block;text-align:right;font-style:normal;color:var(--sky);font-weight:500;margin-top:2px}
  .divider{position:absolute;left:32px;width:202px;border-top:1px dotted #9fb4c8}
  .steps{position:absolute;left:24px;top:271px;width:209px;height:135px;border:1px dashed #8fb0cf;border-radius:10px}
  .pill--steps{left:68px;top:262px;width:122px;height:17px;line-height:17px;font-size:10px;background:var(--sky);font-weight:600}
  .steps ul{list-style:none;position:absolute;left:8px;top:15px;width:196px}
  .steps li{position:relative;padding-left:17px;font-size:7.5px;line-height:12.3px}
  .steps li svg{position:absolute;left:2px;top:2.5px;width:8px;height:8px}
  .steps b{color:var(--blue);font-weight:600}
  .steps .bullet{padding-left:27px;font-weight:600}
  .steps .bullet::before{content:"";position:absolute;left:19px;top:5px;width:3px;height:3px;border-radius:50%;background:#222}
  .steps .wrap{line-height:9.6px;margin-top:3px}
  .contact-title{position:absolute;left:17px;top:430px;font-size:10px;font-weight:600;color:var(--blue)}
  .contact-line{position:absolute;left:108px;top:437px;width:126px;height:1px;background:var(--blue)}
  .contact-icons{position:absolute;left:18px;top:447px;display:flex;gap:5px}
  .contact-icons span{width:11px;height:11px;border-radius:50%;background:var(--sky);display:flex;align-items:center;justify-content:center}
  .contact-details{position:absolute;left:18px;top:462px;font-size:8.6px;line-height:12.5px}
  .contact-details p{margin-bottom:1.5px}
  .badge{position:absolute;left:166px;top:447px;width:66px;height:66px;border-radius:50%;background:var(--sky);border:2px solid var(--teal);color:#fff;font-size:6.3px;font-weight:700;text-align:center;display:flex;align-items:center;justify-content:center;line-height:8px}
  .badge-tab{position:absolute;left:192px;top:510px;width:14px;height:8px;background:var(--navy)}

  /* cover panel */
  .brand{position:absolute;left:30px;top:30px;display:flex;align-items:center;gap:8px}
  .brand-dot{width:26px;height:26px;border-radius:50%;background:#d9dcdf}
  .brand-name{font-family:"Montserrat",sans-serif;font-weight:700;font-size:15px;color:var(--teal)}
  .headline{position:absolute;top:118px;width:100%;text-align:center;font-family:"Oswald",sans-serif;text-transform:uppercase;line-height:46px;letter-spacing:-.5px}
  .headline .light{display:block;color:var(--teal);font-weight:400;font-size:50px}
  .headline .bold{display:block;color:var(--blue);font-weight:600;font-size:50px}
  .cover-photo{position:absolute;left:0;top:272px;width:259px;height:280px;background:linear-gradient(180deg,#f6f3ee 0%,#ece4d6 35%,#cfc6b2 60%,#6d6a58 85%,#3a3c30 100%)}
</style>
</head>
<body>
<main class="brochure">

  <section class="panel panel--about">
    <svg class="portrait" viewBox="0 0 259 200" role="img" aria-label="Portrait photo of the practitioner seated on a sofa">
      <defs>
        <linearGradient id="portraitTone" x1="0" y1="0" x2="0" y2="1">
          <stop offset="0" stop-color="#c9c3bb"/>
          <stop offset="1" stop-color="#8e97a6"/>
        </linearGradient>
      </defs>
      <path d="M0 0H259V150C190 170 90 186 0 168Z" fill="url(#portraitTone)"/>
      <path d="M0 168C90 186 190 170 259 150" fill="none" stroke="var(--sky)" stroke-width="3"/>
      <path d="M0 176C90 192 190 176 259 158" fill="none" stroke="var(--teal)" stroke-width="3"/>
    </svg>
    <h2 class="practitioner-name">DANIEL J ASHFORD</h2>
    <p class="practitioner-creds">FDN-P HPC PFC PBC</p>
    <div class="practitioner-rule"></div>
    <div class="bio">
      <p>Daniel is a multimodality alternative health provider with a focus in shedding light on what holds you back from excellent functional health and showing up as the best version of yourself.</p>
      <p>He will set you up to run bioenergetic scanning at home and facilitate with you functional testing (as necessary), design supporting protocols and lifestyle frameworks to guide you on your path to wellness and beyond.</p>
      <p>It took Daniel almost 3 decades of trial and error, and false hope, for him to arrive at the same conclusion that leading experts in the field of bioenergetics had been saying since the beginning:</p>
      <p><strong>energy drives biochemistry, not the other way round.</strong></p>
      <p>This is foundational to how Lumora Health has become the leading provider of Bioenergetic scanning technology, and how it is helping to restore the energy and subsequent health of the world.</p>
      <p>“in essence, Lumora gives you night goggles on what is going on for you, moreover what you can do about it. This is truly the future of medicine” Daniel J Ashford</p>
      <p>Lumora has evolved over a 20 year period, 100s of 1000s of scans and now the ability for a client to operate the software from home, to either self direct, or operated it under the professional watch of Daniel and his team at vitalhaven.studio</p>
    </div>
    <div class="footer footer--sky">dan@danashford.com</div>
  </section>

  <section class="panel panel--testimonials">
    <div class="pill pill--testimonials">TESTIMONIALS</div>
    <div class="quote-mark">“</div>
    <blockquote class="testimonial" style="top:86px">Thanks to Lumora, my energy has skyrocketed and I am accomplishing more than I have in years<cite>- Karen Whitfield</cite></blockquote>
    <div class="divider" style="top:124px"></div>
    <blockquote class="testimonial" style="top:130px">Lumora Health truly offers insights into the body, both mind and physical well-being, that the medical community cannot comprehend often, nor understand. It is truly a remarkable system<cite>- Dr Helen Marsh</cite></blockquote>
    <div class="divider" style="top:186px"></div>
    <blockquote class="testimonial" style="top:192px">..provides the signal for the body to heal itself. What's hard to understand is it really doesn't do anything except provide the signal. The body does everything else<cite>- Dr. Paul Renner, MD</cite></blockquote>

    <div class="steps">
      <ul>
        <li><svg viewBox="0 0 10 10"><circle cx="5" cy="5" r="4.3" fill="none" stroke="#3176b5"/><path d="M3 5.2l1.5 1.4L7.3 3.6" fill="none" stroke="#3176b5" stroke-width="1.1"/></svg><b>Register</b> - vitalhaven.studio/scan</li>
        <li><svg viewBox="0 0 10 10"><circle cx="5" cy="5" r="4.3" fill="none" stroke="#3176b5"/><path d="M3 5.2l1.5 1.4L7.3 3.6" fill="none" stroke="#3176b5" stroke-width="1.1"/></svg><b>Get Your Scanner</b> - go to shop &amp; buy</li>
        <li><svg viewBox="0 0 10 10"><circle cx="5" cy="5" r="4.3" fill="none" stroke="#3176b5"/><path d="M3 5.2l1.5 1.4L7.3 3.6" fill="none" stroke="#3176b5" stroke-width="1.1"/></svg><b>Download App –</b> VitaPulse</li>
        <li><svg viewBox="0 0 10 10"><circle cx="5" cy="5" r="4.3" fill="none" stroke="#3176b5"/><path d="M3 5.2l1.5 1.4L7.3 3.6" fill="none" stroke="#3176b5" stroke-width="1.1"/></svg>Pair Scanner with your phone</li>
        <li><svg viewBox="0 0 10 10"><circle cx="5" cy="5" r="4.3" fill="none" stroke="#3176b5"/><path d="M3 5.2l1.5 1.4L7.3 3.6" fill="none" stroke="#3176b5" stroke-width="1.1"/></svg>Scan Away (follow instructions)</li>
        <li><svg viewBox="0 0 10 10"><circle cx="5" cy="5" r="4.3" fill="none" stroke="#3176b5"/><path d="M3 5.2l1.5 1.4L7.3 3.6" fill="none" stroke="#3176b5" stroke-width="1.1"/></svg><b>View Results &amp; Information -</b></li>
        <li class="bullet">Online or On Phone</li>
        <li class="wrap"><svg viewBox="0 0 10 10"><circle cx="5" cy="5" r="4.3" fill="none" stroke="#3176b5"/><path d="M3 5.2l1.5 1.4L7.3 3.6" fill="none" stroke="#3176b5" stroke-width="1.1"/></svg>Follow guidelines within software or make an appointment to have bespoke strategy &amp; protocol designed by Daniel</li>
      </ul>
    </div>
    <div class="pill pill--steps">How to Get Started</div>

    <h3 class="contact-title">Contact Us Today</h3>
    <div class="contact-line"></div>
    <div class="contact-icons">
      <span><svg width="7" height="7" viewBox="0 0 10 10"><path d="M2 1.5l2 .2.8 2-1.2.9c.6 1.2 1.4 2 2.6 2.6l.9-1.2 2 .8.2 2C6 9 1 4 2 1.5z" fill="#fff"/></svg></span>
      <span><svg width="7" height="7" viewBox="0 0 10 10"><rect x="1" y="2.5" width="8" height="5.5" fill="none" stroke="#fff"/><path d="M1 2.5l4 3 4-3" fill="none" stroke="#fff"/></svg></span>
      <span><svg width="7" height="7" viewBox="0 0 10 10"><path d="M5 9.5S2 6 2 4a3 3 0 016 0c0 2-3 5.5-3 5.5z" fill="none" stroke="#fff"/><circle cx="5" cy="4" r="1" fill="#fff"/></svg></span>
    </div>
    <div class="contact-details">
      <p>02 9000 4417</p>
      <p>dan@danashford.com</p>
      <p style="line-height:11px">a Level 8, 42 Harbour Lane,<br>Sydney, Australia</p>
    </div>
    <div class="badge-tab"></div>
    <div class="badge">PROVIDING<br>CONVENIENT<br>REMOTE<br>SERVICE ONLY</div>
    <div class="footer footer--blue">www.vitalhaven.studio</div>
  </section>

  <section class="panel panel--cover">
    <div class="cover-photo" role="img" aria-label="Photo of a woman in a white dress at a sunlit seaside, face turned to the sun"></div>
    <div class="brand"><span class="brand-dot"></span><span class="brand-name">VitalHaven.Studio</span></div>
    <h1 class="headline"><span class="light">Restore</span><span class="bold">Your</span><span class="bold">Energy</span></h1>
    <div class="footer footer--navy">Call Us : 02 9000 4417</div>
  </section>

  <svg class="swoosh" viewBox="0 0 777 140" aria-hidden="true">
    <path d="M259 0H478C486 38 510 66 552 74C630 86 712 74 777 56V66C700 96 604 108 518 98C440 88 350 56 259 38Z" fill="var(--sky)"/>
    <path d="M518 114C604 124 702 104 777 70" fill="none" stroke="var(--blue)" stroke-width="3.5"/>
  </svg>
</main>
</body>
</html>
```